Timid Kitten Clinic Business Card Design

I need a business card designed for my cat only veterinary clinic. I will upload the logo that I would like included on the card. Please include:
Business Name: The Timid Kitten Clinic
Address: 4827 W. 39th Ln, Scottsdale, AZ 85317
Phone #: 480-555-6314
Website URL: www.timidkittenvet.example
And the Doctors Name: Marla Quint, DVM

```html
<!DOCTYPE html>
<html lang="en">
<head>
<meta charset="utf-8">
<title>The Timid Kitten Clinic – Business Card</title>
<link rel="stylesheet" href="https://fonts.googleapis.com/css2?family=Lato:wght@400;700&display=swap">
<style>
  :root {
    --page-bg: #e9e6e1;
    --card-bg: #1d1b19;
    --card-edge: #2a2724;
    --accent-green: #3f9a3a;
    --band-green: #46a83f;
    --band-green-dark: #2c7a2a;
    --text-light: #cfc8bd;
    --band-text: #d9d0c2;
    --art-night: #16142a;
    --art-purple: #4b2f7a;
    --art-green: #3c9b46;
  }
  * { margin: 0; padding: 0; box-sizing: border-box; }
  html, body {
    width: 1200px;
    height: 1047px;
    overflow: hidden;
    background: var(--page-bg);
    font-family: "Lato", sans-serif;
  }
  .business-card {
    position: absolute;
    left: 80px;
    top: 239px;
    width: 1040px;
    height: 568px;
    border-radius: 26px;
    background: linear-gradient(180deg, var(--card-edge) 0%, var(--card-bg) 40%, var(--card-bg) 100%);
    overflow: hidden;
  }
  .card-artwork {
    position: absolute;
    left: 106px;
    top: 126px;
    width: 386px;
    height: 313px;
    background:
      linear-gradient(180deg, var(--art-night) 0%, var(--art-night) 55%, var(--art-purple) 70%, var(--art-green) 100%);
  }
  .divider {
    position: absolute;
    left: 537px;
    top: 128px;
    width: 3px;
    height: 312px;
    background: var(--accent-green);
  }
  .details {
    position: absolute;
    left: 575px;
    top: 148px;
    color: var(--text-light);
  }
  .doctor-name {
    font-weight: 700;
    font-size: 37px;
    color: var(--accent-green);
    line-height: 1.2;
    margin-bottom: 56px;
  }
  .address {
    font-size: 23px;
    line-height: 35px;
    margin-bottom: 33px;
  }
  .contact-line {
    display: flex;
    align-items: center;
    gap: 10px;
    font-size: 23px;
    line-height: 37px;
  }
  .contact-line svg { width: 24px; height: 24px; flex: none; }
  .name-band {
    position: absolute;
    left: 0;
    top: 478px;
    width: 100%;
    height: 46px;
    background: linear-gradient(90deg, var(--band-green-dark) 0%, var(--band-green) 25%, var(--band-green) 75%, var(--band-green-dark) 100%);
    text-align: center;
    font-weight: 700;
    font-size: 33px;
    line-height: 46px;
    color: var(--band-text);
  }
</style>
</head>
<body>
  <div class="business-card">
    <div class="card-artwork" role="img" aria-label="Colourful folk-art illustration of a patterned cat perched on a saguaro cactus under a starry night sky with a crescent moon"></div>
    <div class="divider"></div>
    <div class="details">
      <h1 class="doctor-name">Marla Quint, DVM</h1>
      <p class="address">4827 W. 39th Ln,<br>Scottsdale, AZ 85317</p>
      <p class="contact-line">
        <svg viewBox="0 0 24 24" aria-hidden="true"><path fill="#3f9a3a" d="M3 9c0-3 4-5 9-5s9 2 9 5v2h-5V8.5c-1-.6-2.5-.8-4-.8s-3 .2-4 .8V11H3z"/><path fill="#3f9a3a" d="M7 12h10l2 8H5z"/><circle cx="12" cy="15.5" r="2" fill="#1d1b19"/></svg>
        480-555-6314
      </p>
      <p class="contact-line">
        <svg viewBox="0 0 24 24" aria-hidden="true"><circle cx="12" cy="12" r="9" fill="#3f9a3a"/><path fill="#1d1b19" d="M8 6c2 1 1 3 3 3s1 3-1 3-3 2-2 4c-2-1-4-4-3-7 1-1 2-2 3-3zm7 6c2 0 3 1 3 3-1 2-3 3-4 3 0-2-1-3 0-4s0-2 1-2z"/></svg>
        www.timidkittenvet.example
      </p>
    </div>
    <div class="name-band">The Timid Kitten Clinic</div>
  </div>
</body>
</html>
```